Grand Opening for Brightvale Church

Would like to have a BillBoard Created according to the specs listed by the company who will be producing the print. I am attaching the spec sheet to this post. I am also attaching a couple different picture options as well as a former Billboard design that was done. I would like the design to incorporate my logo, picture. I am okay if the background on the picture is eliminated for creative purposes. The words to be displayed is "Grand Opening" April 12, 2020 at the former Harlan Middle School) 41st Copper Lake Rd.

Colors

Designer to choose colors to be used in the design.

Requirements
Must have
• Something that pops
Nice to have
• Good color coordinations and clearly visible text

```html
<!DOCTYPE html>
<html lang="en">
<head>
<meta charset="utf-8">
<title>Brightvale Church – Grand Opening Billboard</title>
<link rel="stylesheet" href="https://fonts.googleapis.com/css2?family=Libre+Baskerville:wght@400;700&family=Montserrat:wght@500;600;700&display=swap">
<style>
  :root {
    --stage: #5e5e5e;
    --board: #f7f7f8;
    --board-shade: #e6e6e8;
    --orange: #f07c12;
    --ink: #2c2b2e;
    --wave: #ffffff;
    --photo-rust: #b4662c;
    --photo-rust-deep: #9c5522;
    --photo-denim: #a3abb4;
  }
  * { box-sizing: border-box; margin: 0; padding: 0; }
  html, body {
    width: 1002px;
    height: 1200px;
    overflow: hidden;
    background: var(--stage);
  }
  .billboard {
    position: absolute;
    left: 31px;
    top: 383px;
    width: 940px;
    height: 433px;
    overflow: hidden;
    background: radial-gradient(ellipse at 35% 40%, #ffffff 0%, var(--board) 55%, var(--board-shade) 100%);
    box-shadow: 0 6px 18px rgba(0,0,0,0.35);
  }
  .billboard__waves {
    position: absolute;
    inset: 0;
    width: 100%;
    height: 100%;
  }
  .headline {
    position: absolute;
    left: 62px;
    top: 36px;
    font-family: "Libre Baskerville", "Times New Roman", serif;
    font-weight: 700;
    font-size: 47px;
    line-height: 1;
    letter-spacing: 0.5px;
    color: var(--orange);
    white-space: nowrap;
  }
  .church-name {
    position: absolute;
    left: 139px;
    top: 132px;
    width: 333px;
    display: flex;
    align-items: center;
    gap: 18px;
  }
  .church-name__dot {
    width: 38px;
    height: 38px;
    border-radius: 50%;
    background: var(--orange);
    flex: none;
  }
  .church-name__text {
    font-family: "Montserrat", Arial, sans-serif;
    font-weight: 600;
    font-size: 46px;
    line-height: 1.08;
    color: var(--ink);
  }
  .event-date {
    position: absolute;
    left: 128px;
    top: 310px;
    width: 355px;
    height: 52px;
    border: 1px solid var(--orange);
    display: flex;
    align-items: center;
    justify-content: center;
    font-family: "Libre Baskerville", "Times New Roman", serif;
    font-size: 33px;
    color: var(--ink);
    white-space: nowrap;
  }
  .venue {
    position: absolute;
    left: 75px;
    top: 379px;
    font-family: "Montserrat", Arial, sans-serif;
    font-size: 18px;
    line-height: 1;
    white-space: nowrap;
    display: flex;
    align-items: center;
    gap: 8px;
  }
  .venue__place { font-weight: 700; color: var(--orange); letter-spacing: 0.3px; }
  .venue__divider { width: 1px; height: 17px; background: var(--ink); }
  .venue__street { font-weight: 500; color: var(--ink); }
  .pastor-photo {
    position: absolute;
    left: 562px;
    top: 28px;
    width: 293px;
    height: 405px;
    border-radius: 18px 18px 0 0;
    background: linear-gradient(180deg, var(--photo-rust) 0%, var(--photo-rust-deep) 70%, var(--photo-denim) 100%);
  }
</style>
</head>
<body>
  <section class="billboard" aria-label="Brightvale Church grand opening billboard">
    <svg class="billboard__waves" viewBox="0 0 940 433" preserveAspectRatio="none" aria-hidden="true">
      <path d="M0 300 C 250 240, 520 330, 940 120" fill="none" stroke="var(--wave)" stroke-width="26" opacity="0.8"/>
      <path d="M0 380 C 300 330, 600 380, 940 230" fill="none" stroke="var(--wave)" stroke-width="18" opacity="0.7"/>
      <path d="M760 0 C 820 90, 880 140, 940 160" fill="none" stroke="#e2e2e4" stroke-width="30" opacity="0.6"/>
      <path d="M0 433 C 200 400, 400 420, 620 433" fill="none" stroke="#e9e9eb" stroke-width="22" opacity="0.6"/>
    </svg>

    <h1 class="headline">GRAND OPENING</h1>

    <div class="church-name">
      <span class="church-name__dot"></span>
      <span class="church-name__text">Brightvale<br>Church</span>
    </div>

    <p class="event-date">APRIL 12, 2020</p>

    <p class="venue">
      <span class="venue__place">HARLAN MIDDLE SCHOOL</span>
      <span class="venue__divider"></span>
      <span class="venue__street">41st Copper Lake Rd.</span>
    </p>

    <div class="pastor-photo" role="img" aria-label="Photo of the pastor in a rust corduroy blazer, striped shirt and jeans, speaking with open hands"></div>
  </section>
</body>
</html>
```